Stonebell Inc Ad Design, trying to attract new customers

Please see attached pictures and files for information
We are a Class A - Residential General Contractor in Lynchburg, VA with Master HVAC and Master PLUMBING Licenses. We focus on Water and Air Solutions for property owners.
We build, remodel, and repair homes
We do HVAC, including Humidity Control and Air Purification
We do Plumbing
We love to fix Water Leaks for Plumbing, Roof Leaks, Skylight Leaks, Basement Leaks, Foundation Leaks, Door and Window Leaks
We solve water and air issues on the outside of properties with custom structures, grading, and landscaping

Target Market(s)

Residential and Light Commercial property owners

Industry/Entity Type

Construction

Font styles to use
Other font styles liked:
• see cards

Colors
0054AA
0677BA
7BADD7
CADEEF
E8F1F8
00AB8E
00BBA5
67D7C9
C6EFE9
E9F9F6

Requirements
Must have
• See business cards
Nice to have
• see business cards
Should not have
• My name

```html
<!DOCTYPE html>
<html lang="en">
<head>
<meta charset="utf-8">
<title>Stonebell Inc – Water and Air Solutions Banner</title>
<link rel="stylesheet" href="https://fonts.googleapis.com/css2?family=Lexend+Exa:wght@300;600;800&family=Poppins:wght@400;500;700&display=swap">
<style>
  :root {
    --stage: #9c9c9c;
    --ink: #1a1a1a;
    --white: #ffffff;
    --green-dark: #1b8a3c;
    --green-light: #5db848;
    --blue-dark: #0054AA;
    --blue-mid: #0677BA;
    --blue-light: #1597d6;
    --tick: #3aa54a;
  }
  * { margin: 0; padding: 0; box-sizing: border-box; }
  html, body { width: 1200px; height: 598px; overflow: hidden; }
  body { background: var(--stage); position: relative; font-family: "Poppins", sans-serif; }

  .banner {
    position: absolute; left: 67px; top: 143px; width: 1066px; height: 310px;
    background: var(--ink); overflow: hidden; color: var(--white);
  }
  .banner-shapes { position: absolute; inset: 0; }

  .brand {
    position: absolute; left: 30px; top: 70px; width: 220px;
    display: flex; align-items: center; justify-content: center; gap: 8px;
    font-family: "Poppins", sans-serif; font-weight: 700; font-size: 21px;
    color: var(--blue-mid); letter-spacing: 0.5px; white-space: nowrap;
  }
  .brand-dot { width: 14px; height: 14px; border-radius: 50%; background: var(--green-dark); }

  .headline { position: absolute; left: 318px; top: 30px; font-family: "Lexend Exa", sans-serif; white-space: nowrap; line-height: 1; }
  .headline-main { font-size: 41px; font-weight: 800; letter-spacing: 0.5px; }
  .headline-main .light { font-weight: 300; }
  .headline-sub { margin-top: 7px; font-size: 28.5px; font-weight: 800; letter-spacing: 0.4px; }

  .focus { position: absolute; left: 318px; top: 127px; font-size: 17.5px; font-weight: 400; white-space: nowrap; letter-spacing: 0.2px; }
  .focus strong { font-weight: 700; }

  .services { position: absolute; list-style: none; font-size: 12.6px; line-height: 15.5px; }
  .services li { position: relative; padding-left: 18px; margin-bottom: 9px; }
  .services li::before {
    content: ""; position: absolute; left: 0; top: 2px; width: 11px; height: 11px; border-radius: 50%;
    background: var(--tick);
  }
  .services li::after {
    content: ""; position: absolute; left: 3.5px; top: 4.5px; width: 3px; height: 5px;
    border: solid var(--white); border-width: 0 1.5px 1.5px 0; transform: rotate(45deg);
  }
  .services-home { left: 322px; top: 175px; width: 320px; }
  .services-leaks { left: 672px; top: 175px; width: 340px; }
  .divider { position: absolute; left: 657px; top: 177px; width: 1px; height: 52px; background: #cfcfcf; }

  .pill {
    position: absolute; left: 0; width: 227px; height: 21px; border-radius: 0 11px 11px 0;
    display: flex; align-items: center; padding-left: 63px; gap: 6px;
    font-size: 14.5px; font-weight: 700; letter-spacing: 0.2px;
  }
  .pill-green { background: linear-gradient(90deg, var(--green-dark), var(--green-light)); }
  .pill-blue { background: linear-gradient(90deg, var(--blue-dark), var(--blue-light)); }
  .pill-icon { flex: none; }
  .pill-build { top: 215px; }
  .pill-remodel { top: 241px; }
  .pill-repair { top: 265px; }

  .contact {
    position: absolute; left: 320px; top: 261px; display: flex; align-items: center; gap: 6px;
    font-family: "Lexend Exa", sans-serif; font-weight: 600; font-size: 18.5px; white-space: nowrap;
  }
  .contact svg { flex: none; }
  .contact .web { margin-left: 8px; }
</style>
</head>
<body>
  <section class="banner" aria-label="Stonebell Inc advertisement banner">
    <svg class="banner-shapes" width="1066" height="310" viewBox="0 0 1066 310" aria-hidden="true">
      <defs>
        <linearGradient id="greenBand" x1="0" x2="1" y1="0" y2="0">
          <stop offset="0" stop-color="#17803a"/>
          <stop offset="1" stop-color="#5cb646"/>
        </linearGradient>
        <linearGradient id="blueBand" x1="0" x2="1" y1="0" y2="0">
          <stop offset="0" stop-color="#0c4f8e"/>
          <stop offset="1" stop-color="#118ed0"/>
        </linearGradient>
        <linearGradient id="tabShade" x1="0" x2="0" y1="0" y2="1">
          <stop offset="0" stop-color="#111"/>
          <stop offset="1" stop-color="#1a1a1a"/>
        </linearGradient>
      </defs>
      <rect x="0" y="0" width="1066" height="157" fill="url(#greenBand)"/>
      <path d="M297 121 H1003 Q1013 121 1013 131 V157 H297 Z" fill="url(#tabShade)"/>
      <path d="M311 249 H1066 V310 H269 L297 263 Q303 249 311 249 Z" fill="url(#blueBand)"/>
      <path d="M276 22 A156 156 0 0 1 146 196" fill="none" stroke="#0677BA" stroke-width="4"/>
      <circle cx="141" cy="41" r="152" fill="#ffffff"/>
    </svg>

    <div class="brand"><span class="brand-dot"></span>STONEBELL INC</div>

    <h1 class="headline">
      <div class="headline-main">MASTER HVAC <span class="light">AND</span></div>
      <div class="headline-sub">MASTER PLUMBING LICENSES</div>
    </h1>

    <p class="focus">WE FOCUS ON <strong>WATER AND AIR SOLUTIONS FOR PROPERTY OWNERS</strong></p>

    <ul class="services services-home">
      <li>HVAC, including Humidity Control<br>and Air Purification , Plumbing</li>
      <li>Custom structures, grading, and landscaping</li>
    </ul>
    <span class="divider"></span>
    <ul class="services services-leaks">
      <li>We fix Water Leaks for Plumbing, Roof Leaks, Skylight Leaks, Basement Leaks, Foundation Leaks, Door and Window Leaks</li>
    </ul>

    <div class="pill pill-green pill-build">
      <svg class="pill-icon" width="12" height="12" viewBox="0 0 12 12" aria-hidden="true"><circle cx="6" cy="6" r="6" fill="#fff"/><path d="M3.3 6.2 5.2 8 8.8 4.2" fill="none" stroke="#1b8a3c" stroke-width="1.6"/></svg>WE BUILD
    </div>
    <div class="pill pill-blue pill-remodel">
      <svg class="pill-icon" width="12" height="12" viewBox="0 0 12 12" aria-hidden="true"><circle cx="6" cy="6" r="6" fill="#fff"/><path d="M3.3 6.2 5.2 8 8.8 4.2" fill="none" stroke="#0054AA" stroke-width="1.6"/></svg>REMODEL
    </div>
    <div class="pill pill-green pill-repair">
      <svg class="pill-icon" width="12" height="12" viewBox="0 0 12 12" aria-hidden="true"><circle cx="6" cy="6" r="6" fill="#fff"/><path d="M3.3 6.2 5.2 8 8.8 4.2" fill="none" stroke="#1b8a3c" stroke-width="1.6"/></svg>REPAIR HOMES
    </div>

    <div class="contact">
      <svg width="16" height="16" viewBox="0 0 16 16" aria-hidden="true"><circle cx="8" cy="8" r="7" fill="none" stroke="#fff" stroke-width="1.6"/><path d="M5.4 4.4c.4-.3.8-.2 1 .2l.6 1.1c.2.3.1.6-.2.9l-.4.3c.4.9 1.1 1.7 2 2.1l.3-.4c.3-.3.6-.3.9-.2l1.1.6c.4.2.5.6.2 1-.5.8-1.3 1.1-2.1.8-1.9-.7-3.3-2.2-4-4.1-.2-.8.1-1.6.6-2.3z" fill="#fff"/></svg>
      <span class="phone">(434) 555-0182</span>
      <svg class="web" width="16" height="16" viewBox="0 0 16 16" aria-hidden="true"><g fill="none" stroke="#fff" stroke-width="1.4"><circle cx="8" cy="8" r="6.6"/><ellipse cx="8" cy="8" rx="2.8" ry="6.6"/><path d="M1.6 8h12.8M2.6 4.8h10.8M2.6 11.2h10.8"/></g></svg>
      <span>www.BuiltInTheBreeze VA.com</span>
    </div>
  </section>
</body>
</html>
```